Garage Flooring Flyer

We are looking for a flyer design for our garage flooring company. We specialise in installing garage floor coatings. We use industrial grade products and are serious about durability and quality.
We target male car enthusiasts and want to project the image of a modern high-tech company. The flyer should be stunningly visual and incorporate the logo and photos we have attached. Other photos or images are welcomed.
Some key mentions to be made on the flyer are listed below:
About Us
"We are K*** R***** LLC, Home of the garage enthusiasts and Waukesha’s premier garage floor installer"
Services
Garage Floor Coatings
Offers
-Call or Email for a FREE estimate!
Credentials
-QN logo
-Pictavo Logo
-Zorbin Logo
-5stars?
Benefit Highlights to be mentioned or listed (not in any particular order)
-Industrial Quality and Strength
-Easy to Clean
-Many Color Options
-Locally Owned and Operated
-Satisfaction Guaranteed
-Lifetime Limited Warranty
-Increases Home Value
-MAKE YOUR FRIENDS AND NEIGHBORS JEALOUS!
-Fully Insured
-Certified and Trusted Installer
-Oil and Chemical Resistant
-UV Stable
-Impact and Abrasion Resistant
Contact Info
-Phone
-Email
-Website
Captions
-"From diamond grinding surface prep to using only the highest industrial-grade products, we believe in taking the time to ensure a proper installation and guarantee a durable long-lasting and beautiful garage floor";
-Serving Southeastern Wisconsin!

```html
<!DOCTYPE html>
<html lang="en">
<head>
<meta charset="utf-8">
<title>K*** R***** LLC – Garage Floor Flyer</title>
<link rel="stylesheet" href="https://fonts.googleapis.com/css2?family=Oswald:wght@500;600;700&family=Playfair+Display:ital,wght@1,800;1,900&family=Montserrat:wght@400;600;700&display=swap">
<style>
  :root{
    --backdrop-light:#e4e4e4;
    --backdrop-dark:#8a8a8a;
    --paper:#ffffff;
    --ink:#111111;
    --tan:#a88d68;
    --tan-light:#c9ab82;
    --panel:#2a2623;
    --band-a:#4a4038;
    --band-b:#2f2a26;
    --black:#050505;
    --white:#ffffff;
  }
  *{box-sizing:border-box;margin:0;padding:0}
  html,body{width:1200px;height:1200px;overflow:hidden}
  body{background:radial-gradient(ellipse at center,var(--backdrop-light) 0%,var(--backdrop-dark) 100%);position:relative;font-family:'Montserrat',sans-serif}
  .flyer{position:absolute;left:175px;top:0;width:848px;height:1200px;background:var(--paper);overflow:hidden}
  .abs{position:absolute}

  /* header */
  .brand{left:46px;top:62px;white-space:nowrap;font-family:'Oswald',sans-serif;font-weight:700;font-size:38px;line-height:1;color:var(--ink);letter-spacing:1px}
  .brand-mark{display:inline-block;width:16px;height:16px;background:var(--ink);margin-right:10px;vertical-align:middle}
  .estimate{right:34px;top:40px;text-align:right;font-family:'Oswald',sans-serif;font-weight:700;letter-spacing:-1px;line-height:.95}
  .estimate .line1{font-size:56px;color:var(--ink)}
  .estimate .line2{font-size:43px;color:var(--tan)}

  /* hero */
  .hero-photo{left:0;top:170px;width:548px;height:662px;background:linear-gradient(170deg,#5b534b 0%,#8f877c 35%,#b3aca2 60%,#d9d4cc 100%)}
  .headline{left:40px;top:222px;width:460px;font-family:'Oswald',sans-serif;font-weight:600;line-height:1;text-shadow:0 2px 6px rgba(0,0,0,.5)}
  .headline .city{font-family:'Playfair Display',serif;font-style:italic;font-weight:900;font-size:58px;color:var(--white);margin-bottom:12px}
  .headline .tan{color:var(--tan-light);font-size:56px;letter-spacing:-1px;margin-bottom:8px;padding-left:6px}
  .headline .tan.second{padding-left:17px}
  .headline .big{color:var(--white);font-size:76px;letter-spacing:-2px;padding-left:16px}
  .jealous{left:22px;top:520px;width:340px;text-align:center;font-family:'Playfair Display',serif;font-style:italic;font-weight:800;font-size:28px;line-height:1.22;color:var(--ink);letter-spacing:-1px;text-shadow:0 0 14px #fff,0 0 24px #fff}
  .stars{left:80px;top:658px;width:212px;height:42px}

  /* services panel */
  .services{left:548px;top:170px;width:300px;height:662px;background:linear-gradient(180deg,#24201d,var(--panel) 60%,#3a332d)}
  .row{position:absolute;left:0;width:300px;display:flex;align-items:center;justify-content:flex-end;padding-right:14px;font-weight:700;font-size:19px;line-height:1.1;color:var(--white);text-align:right;letter-spacing:.5px}
  .row.a{background:var(--band-a)}
  .row.b{background:var(--band-b)}
  .row svg{width:26px;height:26px;margin-left:12px;flex:none}
  .assure{left:548px;top:562px;width:300px;text-align:center;font-family:'Oswald',sans-serif;font-weight:600;color:var(--tan-light);font-size:33px;line-height:1}
  .assure .gap{margin-bottom:10px}
  .specs{left:548px;top:698px;width:300px;text-align:center;font-weight:700;font-size:14.5px;line-height:1.04}
  .specs .w{color:var(--white)}
  .specs .t{color:var(--tan-light)}

  /* benefits */
  .benefits-band{left:0;top:832px;width:848px;height:298px;background:var(--black)}
  .benefits-title{left:38px;top:858px;font-family:'Oswald',sans-serif;font-weight:600;font-size:37px;line-height:44px;letter-spacing:-1px;color:var(--tan)}
  .benefits-list{left:38px;top:903px;list-style:none;font-size:18px;line-height:26.4px;color:var(--white);letter-spacing:.2px;white-space:nowrap}
  .samples{left:400px;top:864px;width:420px;height:112px;transform:skewX(-12deg);background:linear-gradient(90deg,#6d604e,#4e4f51,#2c2c2d,#9a8a6c,#b8a079,#a38f72,#7a7d80,#a7a6a2,#8a8c8e,#c0c1bd);border:3px solid #f2f2f2}
  .caption{left:370px;top:1010px;width:452px;text-align:center;font-size:16px;line-height:22px;color:var(--white)}

  /* footer */
  .footer{left:0;top:1130px;width:848px;height:70px;background:linear-gradient(180deg,#b39a74,var(--tan))}
  .footer-item{position:absolute;top:1140px;font-family:'Oswald',sans-serif;font-weight:600;font-size:36px;line-height:50px;color:var(--ink);letter-spacing:-1px;white-space:nowrap}
  .phone{left:45px}
  .site{left:335px}
  .socials{position:absolute;left:690px;top:1150px;display:flex;gap:10px;font-family:'Oswald',sans-serif;font-weight:600;font-size:19px;line-height:30px;color:var(--ink);white-space:nowrap}
</style>
</head>
<body>
<main class="flyer">

  <header>
    <div class="abs brand"><span class="brand-mark"></span>K*** R***** LLC</div>
    <div class="abs estimate">
      <div class="line1">CALL OR EMAIL</div>
      <div class="line2">FOR A FREE ESTIMATE!</div>
    </div>
  </header>

  <section class="hero">
    <div class="abs hero-photo" role="img" aria-label="Finished flake epoxy garage floor with grey cabinets and a black sports car parked inside"></div>
    <h1 class="abs headline">
      <div class="city">Waukesha's</div>
      <div class="tan">PREMIER EPOXY</div>
      <div class="tan second">GARAGE FLOOR</div>
      <div class="big">INSTALLER</div>
    </h1>
    <p class="abs jealous">MAKE YOUR FRIENDS AND NEIGHBORS JEALOUS!</p>
    <svg class="abs stars" viewBox="0 0 212 42" aria-label="Five star rating">
      <defs>
        <linearGradient id="starFill" x1="0" y1="0" x2="0" y2="1">
          <stop offset="0" stop-color="#ffd75a"/><stop offset="1" stop-color="#f0a020"/>
        </linearGradient>
        <polygon id="star" points="20,2 25.3,14.6 39,15.8 28.6,24.8 31.8,38.2 20,31 8.2,38.2 11.4,24.8 1,15.8 14.7,14.6"/>
      </defs>
      <use href="#star" x="0" fill="url(#starFill)"/>
      <use href="#star" x="43" fill="url(#starFill)"/>
      <use href="#star" x="86" fill="url(#starFill)"/>
      <use href="#star" x="129" fill="url(#starFill)"/>
      <use href="#star" x="172" fill="url(#starFill)"/>
    </svg>
  </section>

  <aside class="abs services">
    <div class="row a" style="top:64px;height:48px">Epoxy<br>Garage Floors<svg viewBox="0 0 26 26"><path d="M3 14 L10 21 L23 4" fill="none" stroke="#fff" stroke-width="3.4" stroke-linecap="round" stroke-linejoin="round"/></svg></div>
    <div class="row b" style="top:112px;height:68px">Epoxy Flake<br>Garage Floors<svg viewBox="0 0 26 26"><path d="M3 14 L10 21 L23 4" fill="none" stroke="#fff" stroke-width="3.4" stroke-linecap="round" stroke-linejoin="round"/></svg></div>
    <div class="row a" style="top:180px;height:50px">Metallic<br>Garage Floors<svg viewBox="0 0 26 26"><path d="M3 14 L10 21 L23 4" fill="none" stroke="#fff" stroke-width="3.4" stroke-linecap="round" stroke-linejoin="round"/></svg></div>
    <div class="row b" style="top:230px;height:50px">Storage Solutions<svg viewBox="0 0 26 26"><path d="M3 14 L10 21 L23 4" fill="none" stroke="#fff" stroke-width="3.4" stroke-linecap="round" stroke-linejoin="round"/></svg></div>
    <div class="row a" style="top:280px;height:50px">Garage Floor<br>Alternatives<svg viewBox="0 0 26 26"><path d="M3 14 L10 21 L23 4" fill="none" stroke="#fff" stroke-width="3.4" stroke-linecap="round" stroke-linejoin="round"/></svg></div>
    <div class="row b" style="top:330px;height:44px">Custom Logos<svg viewBox="0 0 26 26"><path d="M3 14 L10 21 L23 4" fill="none" stroke="#fff" stroke-width="3.4" stroke-linecap="round" stroke-linejoin="round"/></svg></div>
  </aside>
  <div class="abs assure">
    <div class="gap">FULLY INSURED</div>
    <div>CERTIFIED AND</div>
    <div>TRUSTED INSTALLER</div>
  </div>
  <div class="abs specs">
    <div class="w">CERTIFIED AND<br>TRUSTED INSTALLER</div>
    <div class="t">OIL AND CHEMICAL<br>RESISTANT</div>
    <div class="w">UV STABLE - WON'T YELLOW</div>
    <div class="t">IMPACT AND<br>ABRASION RESISTANT</div>
  </div>

  <section>
    <div class="abs benefits-band"></div>
    <h2 class="abs benefits-title">BENEFIT HIGHLIGHTS</h2>
    <ul class="abs benefits-list">
      <li>-Industrial Quality and Strength</li>
      <li>-Easy to Clean</li>
      <li>-Many Color Options</li>
      <li>-Locally Owned and Operated</li>
      <li>-Satisfaction Guaranteed</li>
      <li>-Lifetime Limited Warranty</li>
      <li>-Satisfaction Guaranteed</li>
      <li>-Increases Home Value</li>
    </ul>
    <div class="abs samples" role="img" aria-label="Fanned row of flake floor colour samples in tan, grey, black and white blends"></div>
    <p class="abs caption">From diamond grinding surface prep to using only the highest industrial-grade products, we believe in taking the time to ensure a proper installation and guarantee a durable long-lasting and beautiful garage floor</p>
  </section>

  <footer>
    <div class="abs footer"></div>
    <div class="footer-item phone">(262) 555-0148</div>
    <div class="footer-item site">KRGARAGEFLOORS.COM</div>
    <div class="socials"><span>QN</span><span>Pictavo</span><span>Zorbin</span></div>
  </footer>

</main>
</body>
</html>
```